Doors for Chiropractic Office

In my chiropractic office I have 6 treatment rooms and 2 massage rooms. The entire office is going through a remodel. The overall color scheme is very earth tones but in order to add some color, the 6 doors to the treatment rooms will all be a separate color (Red, Blue, Yellow, Green etc)
I need to number each room 1,2,3,4,5,6 and the 2 massage rooms. I had the idea of putting a giant number on each door, so I am looking for some graphic ideas for that project.
The rooms are located with 4 on each side of a long hallway with the 2 massage rooms at the end.
The purpose of numbering each door is to direct the patients where to go.
I have uploaded pictures of the hall way. Pardon the dust since we are under construction but hopefully it gives you an idea of the layout. The door colors will change as stated above.

Requirements
Nice to have
• I would like to see someone come up with a design where each number for the doors are created out of vertebrae's.

```html
<!DOCTYPE html>
<html lang="en">
<head>
<meta charset="UTF-8">
<title>Door Signs – Treatment and Massage Rooms</title>
<link href="https://fonts.googleapis.com/css2?family=Anton&display=swap" rel="stylesheet">
<style>
  :root {
    --bg-light: #ffffff;
    --bg-dark: #a9a9a9;
    --red: #d63138;
    --blue: #35aae0;
    --yellow: #fbd426;
    --green: #14a050;
    --brown: #7b4530;
    --grey: #6b6b6c;
    --olive: #899742;
    --ochre: #9c7a3c;
    --white: #ffffff;
    --shade: rgba(0, 0, 0, 0.14);
  }
  * { margin: 0; padding: 0; box-sizing: border-box; }
  html, body { width: 1200px; height: 429px; overflow: hidden; }
  body {
    position: relative;
    background: linear-gradient(160deg, var(--bg-light) 0%, var(--bg-light) 30%, #e4e4e4 60%, var(--bg-dark) 100%);
    font-family: "Anton", "Arial Narrow", sans-serif;
  }
  .door {
    position: absolute;
    top: 99px;
    width: 115px;
    height: 230px;
    background: var(--door);
    box-shadow: 1px 2px 4px rgba(0, 0, 0, 0.35);
  }
  .door--red { --door: var(--red); left: 77px; }
  .door--blue { --door: var(--blue); left: 205px; }
  .door--yellow { --door: var(--yellow); left: 334px; }
  .door--green { --door: var(--green); left: 462px; }
  .door--brown { --door: var(--brown); left: 591px; }
  .door--grey { --door: var(--grey); left: 719px; }
  .door--olive { --door: var(--olive); left: 881px; }
  .door--ochre { --door: var(--ochre); left: 1007px; }

  /* Treatment room plate */
  .room-plate {
    position: absolute;
    left: 21px; top: 25px;
    width: 73px; height: 45px;
    border: 1px solid var(--white);
    border-radius: 1px;
    padding: 3px;
    display: flex;
  }
  .room-plate__label {
    width: 22px;
    background: var(--shade);
    display: flex; align-items: center; justify-content: center;
  }
  .room-plate__label span {
    transform: rotate(-90deg);
    color: var(--white);
    font-size: 13px;
    letter-spacing: 0.3px;
    line-height: 1;
  }
  .room-plate__number {
    flex: 1;
    background: var(--white);
    color: var(--door);
    font-size: 34px;
    line-height: 37px;
    text-align: center;
    letter-spacing: -0.5px;
  }

  /* Massage room plate */
  .massage-plate {
    position: absolute;
    left: 21px; top: 20px;
    width: 73px; height: 45px;
    border: 1px solid var(--white);
    border-radius: 1px;
    padding: 3px;
  }
  .massage-plate__number {
    height: 100%;
    background: var(--white);
    color: var(--door);
    font-size: 35px;
    line-height: 38px;
    text-align: center;
  }
  .massage-plate__label {
    position: absolute;
    left: 25px; top: 59px;
    width: 65px; height: 29px;
    background: var(--shade);
    color: var(--white);
    font-size: 12.5px;
    line-height: 12.5px;
    text-align: center;
    padding-top: 2px;
  }

  /* Practice name */
  .brand {
    position: absolute;
    left: 58px; top: 203px;
    display: flex; align-items: center; gap: 3px;
    color: var(--white);
  }
  .brand__dot {
    width: 11px; height: 11px;
    border-radius: 50%;
    background: var(--white);
    opacity: 0.85;
  }
  .brand__name {
    font-size: 5px;
    line-height: 5.5px;
    letter-spacing: 0.2px;
    text-transform: uppercase;
  }
</style>
</head>
<body>

  <section class="door door--red" aria-label="Room 01 door">
    <div class="room-plate"><div class="room-plate__label"><span>ROOM</span></div><div class="room-plate__number">01</div></div>
    <div class="brand"><div class="brand__dot"></div><div class="brand__name">Meadow<br>Spine Care</div></div>
  </section>

  <section class="door door--blue" aria-label="Room 02 door">
    <div class="room-plate"><div class="room-plate__label"><span>ROOM</span></div><div class="room-plate__number">02</div></div>
    <div class="brand"><div class="brand__dot"></div><div class="brand__name">Meadow<br>Spine Care</div></div>
  </section>

  <section class="door door--yellow" aria-label="Room 03 door">
    <div class="room-plate"><div class="room-plate__label"><span>ROOM</span></div><div class="room-plate__number">03</div></div>
    <div class="brand"><div class="brand__dot"></div><div class="brand__name">Meadow<br>Spine Care</div></div>
  </section>

  <section class="door door--green" aria-label="Room 04 door">
    <div class="room-plate"><div class="room-plate__label"><span>ROOM</span></div><div class="room-plate__number">04</div></div>
    <div class="brand"><div class="brand__dot"></div><div class="brand__name">Meadow<br>Spine Care</div></div>
  </section>

  <section class="door door--brown" aria-label="Room 05 door">
    <div class="room-plate"><div class="room-plate__label"><span>ROOM</span></div><div class="room-plate__number">05</div></div>
    <div class="brand"><div class="brand__dot"></div><div class="brand__name">Meadow<br>Spine Care</div></div>
  </section>

  <section class="door door--grey" aria-label="Room 06 door">
    <div class="room-plate"><div class="room-plate__label"><span>ROOM</span></div><div class="room-plate__number">06</div></div>
    <div class="brand"><div class="brand__dot"></div><div class="brand__name">Meadow<br>Spine Care</div></div>
  </section>

  <section class="door door--olive" aria-label="Massage room 01 door">
    <div class="massage-plate"><div class="massage-plate__number">01</div></div>
    <div class="massage-plate__label">MASSAGE<br>ROOM</div>
    <div class="brand"><div class="brand__dot"></div><div class="brand__name">Meadow<br>Spine Care</div></div>
  </section>

  <section class="door door--ochre" aria-label="Massage room 02 door">
    <div class="massage-plate"><div class="massage-plate__number">02</div></div>
    <div class="massage-plate__label">MASSAGE<br>ROOM</div>
    <div class="brand"><div class="brand__dot"></div><div class="brand__name">Meadow<br>Spine Care</div></div>
  </section>

</body>
</html>
```